依頼詳細
今回作成するチラシは朝凪新報様へ折込む集客チラシの作成です。
しっかり集客ができる動線で作っていただきたいです。
「集客」という目標が最大限できれば、それ以外は求めません。
ターゲットは50代夫婦で子供は独立している方々です。お金は多少余裕があり、お庭の雑草対策に悩んでいる方へ最新技術の雑草の生えない人工芝をしっかりアピール(集客)したいです。
また、このチラシで集客するために、訪問見積もりご依頼いただいたお客様対象「限定15名 スパークリングワイン&スペシャルグラスプレゼント」キャンペーンをする予定です。
スパークリングワイン1本とスペシャルグラス2つプレゼントです。URLは以下の通りです。

https://www.kaimono-ichiba.example/[ルミオン]Lumion-フルートグラス-ステムレスグラスセット/dp/X00000001/

https://www.kaimono-ichiba.example/コルネット-厳選泡6本セット-750mlx6本ワインセット/dp/X00000002/
記載項目
社名:緑野芝生工房株式会社 / 電話:0120-555-318 / URL:tobu-lawn.example
サイズ
A4
ページ数
片面
希望イメージ
シンプル 複雑
単色 カラフル
暗い 明るい
日常 高級
遊び心 厳粛
未来的 伝統的
女性的 男性的
希望する色
緑系、集客さえできるチラシであれば何色を使っても正解です。
補足説明
必要な画像は弊社ホームページからいくらでも転用ください。
そのほか必要な画像は申しつけください。
追加でイメージをお伝えします。
新聞購読者が弊社折込チラシをパッと見て捨てないデザイン(インパクト・限定感・わかりやすさ)で、
電話番号大きくして「今すぐ電話しよう!」と自然とすぐ行動するような導線にしてください。
データを参考に添付します。
【仕様変更】

依頼内容の大幅な変更をお願いいたします。
キャンペーン「スパークリング ワイン・グラスプレゼント」は中止となりました。
もうすでにお取り組みされておられるランサーの方々には大変申し訳ございませんが、「スパークリングワイン・グラスプレゼント」は記載しないようお願いいたします。
また、その代わりにキャンペーン文言「もうすぐ完売! 【キャンペーンプラン】」というように訴求くださると助かります。(訴求のためでしたら追加で【急げ!】【期間限定!】等を追加で入れても問題ございません。)

「もうすぐ完売! 【キャンペーンプラン】」について補足いたします。
弊社では人工芝工事に「エコノミープラン」「ビジネスプラン」「ファーストクラスプラン」がありますが、
キャンペーンプランは通常の「ビジネスプラン」より約21,000円お安く工事が可能なプランです。
(上記のプランの説明を入れることは必須ということではございません。あくまでランサー様へご理解いただくため記載申し上げました。)
内容が大幅に変更となったこと、重ねてお詫び申し上げます。
■ 選んだ理由

訴求から問い合わせまでの動線と内容がよく、木になる人にも情報を提供していたため、デザインだけでなく、情報提供力に優れていたからです。

■ 提案者全員のお礼・コメント

ご提案くださりました全ての方々に、御礼申し上げます。
次回以降ももし可能でしたら優秀な皆様にまたご提案いただけますと嬉しい限りでございます。

```html
<!DOCTYPE html>
<html lang="ja">
<head>
<meta charset="utf-8">
<title>10年人工芝 集客チラシ</title>
<link rel="stylesheet" href="https://fonts.googleapis.com/css2?family=Noto+Sans+JP:wght@400;500;700;900&family=Zen+Old+Mincho:wght@700;900&display=swap">
<style>
:root{
  --green:#2f8a3a;
  --green-dark:#1f6a2a;
  --yellow:#ffe100;
  --gold:#c9a54a;
  --ink:#222;
  --white:#fff;
  --paper:#f4f4f1;
  --red:#d2461f;
}
*{margin:0;padding:0;box-sizing:border-box}
html,body{width:846px;height:1200px;overflow:hidden;background:var(--white)}
body{font-family:"Noto Sans JP",sans-serif;color:var(--ink)}
.flyer{position:relative;width:846px;height:1200px;overflow:hidden;background:var(--white)}

/* hero */
.hero{position:absolute;left:0;top:0;width:846px;height:648px;overflow:hidden}
.hero-photo{position:absolute;inset:0;
  background:
    radial-gradient(ellipse 260px 200px at 110px 170px,rgba(70,120,50,.85),rgba(70,120,50,0) 70%),
    radial-gradient(ellipse 300px 150px at 560px 230px,rgba(242,236,222,.95),rgba(242,236,222,0) 75%),
    linear-gradient(90deg,rgba(0,0,0,0) 45%,rgba(190,160,110,.55) 60%,rgba(0,0,0,0) 95%),
    linear-gradient(180deg,#cfe4ee 0%,#b9d4c4 18%,#8fb078 32%,#a9b892 40%,#6faa3d 46%,#5e9d30 70%,#4a8722 100%)}
.hero-shade{position:absolute;left:0;right:0;top:250px;height:260px;
  background:linear-gradient(180deg,rgba(0,0,0,0),rgba(0,0,0,.18) 50%,rgba(0,0,0,0))}
.brand{position:absolute;left:0;top:0;width:150px;height:118px;background:var(--white);
  display:flex;flex-direction:column;align-items:center;justify-content:center;gap:6px}
.brand-mark{width:34px;height:34px;background:var(--green)}
.brand-name{font-size:15px;font-weight:700;color:var(--green-dark);letter-spacing:.05em}
.awards{position:absolute;right:22px;top:14px;display:flex;gap:14px}
.award{width:100px;height:100px;border-radius:50%;background:radial-gradient(circle at 40% 35%,#3a3a3a,#111);
  border:4px solid var(--gold);display:flex;flex-direction:column;align-items:center;justify-content:center;
  color:var(--gold);text-align:center;line-height:1.15}
.award-rank{font-size:20px;font-weight:900;color:#f1d98a}
.award-label{font-size:11px;font-weight:700;color:var(--white)}
.award-note{position:absolute;right:22px;top:122px;width:214px;font-size:9px;line-height:1.4;color:#333;text-align:right}
.tagline{position:absolute;left:0;right:0;top:282px;display:flex;justify-content:center;align-items:center;gap:18px}
.tagline span{font-size:36px;font-weight:700;color:var(--white);letter-spacing:.06em;text-shadow:0 2px 6px rgba(0,0,0,.5)}
.tagline i{display:block;width:120px;height:2px;background:var(--white)}
.headline{position:absolute;left:0;right:0;top:340px;text-align:center;font-weight:900;color:var(--yellow);
  font-size:130px;line-height:1;letter-spacing:.02em;text-shadow:0 4px 12px rgba(0,0,0,.55)}
.headline small{font-size:92px}

/* features */
.features{position:absolute;left:0;top:648px;width:846px;height:250px;background:var(--paper)}
.features-title{margin:10px auto 0;width:800px;height:46px;background:var(--green);color:var(--white);
  font-size:25px;font-weight:900;text-align:center;line-height:46px;letter-spacing:.04em}
.feature-list{display:flex;gap:10px;justify-content:center;margin-top:10px}
.feature{width:193px;background:var(--white);border:2px solid var(--green);padding:4px}
.feature h3{font-size:15px;font-weight:700;color:var(--red);text-align:center;line-height:22px}
.feature-photo{height:118px;background:linear-gradient(180deg,#9cc36a,#4c8a26)}
.feature p{font-size:10px;text-align:center;line-height:18px}

/* campaign */
.campaign{position:absolute;left:18px;top:904px;width:810px;height:98px;background:var(--white);
  border:3px solid var(--green);display:flex;align-items:center}
.soldout{position:absolute;left:-6px;top:-6px;width:104px;height:104px;border-radius:50%;background:var(--yellow);
  display:flex;flex-direction:column;align-items:center;justify-content:center;font-weight:900;color:var(--red);font-size:17px;line-height:1.2}
.campaign-plan{margin-left:120px;font-family:"Zen Old Mincho",serif;font-weight:900;color:var(--green);font-size:40px;letter-spacing:.02em}
.campaign-note{display:block;font-family:"Noto Sans JP",sans-serif;font-size:11px;font-weight:500;color:#555;letter-spacing:0;text-align:right}
.campaign-price{margin-left:auto;margin-right:22px;font-family:"Zen Old Mincho",serif;font-weight:900;color:var(--green);font-size:44px}
.campaign-price small{font-size:28px}

/* contact */
.contact{position:absolute;left:18px;top:1016px;width:810px}
.contact-row{display:flex;align-items:baseline;gap:24px;border-bottom:2px solid var(--green);padding-bottom:8px}
.company{font-size:24px;font-weight:900;color:var(--green-dark)}
.address,.url{font-size:14px}
.url{margin-left:auto}
.tel-row{display:flex;align-items:center;margin-top:12px}
.tel-icon{width:76px;height:56px}
.tel{font-size:74px;font-weight:900;color:var(--green-dark);letter-spacing:.01em;line-height:1;margin-left:12px}
.hours{margin-left:auto;border:2px solid var(--green);padding:6px 12px;font-size:14px;line-height:1.5}
.hours b{color:var(--green-dark)}
</style>
</head>
<body>
<div class="flyer">
  <section class="hero">
    <div class="hero-photo" role="img" aria-label="人工芝の庭で遊ぶ家族とウッドデッキのある白い家の写真"></div>
    <div class="hero-shade"></div>
    <div class="brand"><div class="brand-mark"></div><div class="brand-name">緑野芝生工房</div></div>
    <div class="awards">
      <div class="award"><span class="award-rank">No.1</span><span class="award-label">人工芝<br>施工部門</span></div>
      <div class="award"><span class="award-rank">No.1</span><span class="award-label">お客様<br>満足度</span></div>
    </div>
    <p class="award-note">※専門調査機関による顧客満足度調査の結果に基づく評価</p>
    <div class="tagline"><i></i><span>うちの芝生は青い…</span><i></i></div>
    <h1 class="headline">10<small>年</small>人工芝</h1>
  </section>

  <section class="features">
    <h2 class="features-title">雑草が生えない! 安心・安全な施工技術</h2>
    <div class="feature-list">
      <div class="feature"><h3>景観の良さ</h3><div class="feature-photo" role="img" aria-label="青々とした人工芝の庭"></div><p>青々と美しい一年中の景色</p></div>
      <div class="feature"><h3>下地処理</h3><div class="feature-photo" role="img" aria-label="人工芝の下地施工の様子"></div><p>雑草をしっかり抑える下地</p></div>
      <div class="feature"><h3>品質の高さ</h3><div class="feature-photo" role="img" aria-label="人工芝の芝葉のアップ"></div><p>ふかふかの肌触り</p></div>
      <div class="feature"><h3>豊富なカラー</h3><div class="feature-photo" role="img" aria-label="色違いの人工芝サンプル"></div><p>デザイン芝生で多彩な色</p></div>
    </div>
  </section>

  <section class="campaign">
    <div class="soldout"><span>もうすぐ</span><span>完売!</span></div>
    <div class="campaign-plan">キャンペーンプラン<span class="campaign-note">ビジネスプラン通常価格より</span></div>
    <div class="campaign-price"><small>約</small>21,000<small>円OFF</small></div>
  </section>

  <footer class="contact">
    <div class="contact-row">
      <span class="company">緑野芝生工房株式会社</span>
      <span class="address">埼玉県青葉市若草町3-4-5</span>
      <span class="url">https://tobu-lawn.example</span>
    </div>
    <div class="tel-row">
      <svg class="tel-icon" viewBox="0 0 76 56" aria-hidden="true">
        <rect x="0" y="0" width="76" height="56" rx="10" fill="#2f8a3a"/>
        <path d="M26 14c3 0 5 6 4 8l-3 3c2 5 6 9 11 11l3-3c2-1 8 1 8 4v4c0 2-2 3-4 3C31 44 22 35 22 19c0-2 1-5 4-5z" fill="#fff"/>
      </svg>
      <span class="tel">0120-555-318</span>
      <div class="hours"><b>【営業時間】</b><br>平日9:00〜20:00</div>
    </div>
  </footer>
</div>
</body>
</html>
```